Creative, Fun, Eye catching signage for new office - inspire and inform!

I am looking for a billboard sign, a smaller sign and a very small sign for parking spots. These will be located in our new office space. I have uploaded two logos, this way you can choose. I would love to see what it looks like with black behind the logo but am open to creative ideas. I would like the majority of the background to be black and/or white

1. Sign for over door – with five at the top like in the photo attached

The sign size is 2600mm (L) x 900mm (H)

Logo at the top then services to the right side
Social & Living Skills Programs
Support Workers
Respite/Supported Holidays
Exercise Physiology
Occupational Therapy
Speech Therapy
Psychology
Behavioural Therapy

I would like the design to tie in with the website and/or flyers/banners attached. Please also try and add 1800 527 930

2. Sign for glass roller door

745cm wide by 725cm high ( similar to what next door has without it saying parent )

Tallbrook Logo
Drop Off Zone

Smaller signs for parking spots
1000cm wide, 60cm high

Tallbrook logo Visitor Parking 24/7

I would like the design to be consistent across the three items so they work together but are not identical.

I have attached images showing what I am talking about in relation to the location of each sign.

Target Market(s)

Families, parents and people with disabilities

Industry/Entity Type

Disability and community service

Colors

Designer to choose colors to be used in the design.

Requirements
Must have
• White or black background - the logo and please use colours shown in the brochures and banners provided. Preferences are black white and yellow
Nice to have
• all of our services and website and/or 1800 527 930 on banner 1
Should not have
• I dont want it to be to busy please

```html
<!DOCTYPE html>
<html lang="en">
<head>
<meta charset="utf-8">
<title>Tallbrook Signage Set</title>
<link rel="stylesheet" href="https://fonts.googleapis.com/css2?family=Poppins:wght@400;500;600;700;800&display=swap">
<style>
  :root {
    --stage: #717171;
    --ink: #1a1d1e;
    --paper: #ffffff;
    --pink: #e0405f;
    --pink-deep: #c92f4f;
    --sun: #ffd95a;
    --sun-line: #e3dc3c;
    --sky: #3b8fe0;
    --rule: #d4d4d4;
    --label: #f2f2f2;
  }
  * { box-sizing: border-box; margin: 0; padding: 0; }
  html, body { width: 1200px; height: 2417px; overflow: hidden; }
  body {
    background: var(--stage);
    font-family: "Poppins", sans-serif;
    position: relative;
  }
  .size-label {
    position: absolute; left: 0; width: 1200px; text-align: center;
    color: var(--label); font-size: 26px; font-weight: 500; letter-spacing: 0.5px;
  }
  .sign { position: absolute; background: var(--paper); overflow: hidden; box-shadow: 0 2px 6px rgba(0,0,0,0.25); }
  .sign svg.backdrop { position: absolute; left: 0; top: 0; }

  /* Door sign */
  .door-sign { left: 76px; top: 296px; width: 1049px; height: 363px; }
  .brand-dot { position: absolute; border-radius: 50%; background: var(--sun); }
  .door-sign .brand-dot { left: 174px; top: 48px; width: 52px; height: 52px; }
  .brand-name { position: absolute; font-weight: 700; text-align: center; white-space: nowrap; }
  .door-sign .brand-name { left: 0; width: 398px; top: 104px; font-size: 62px; color: var(--paper); line-height: 1; }
  .phone-pill {
    position: absolute; left: 42px; top: 222px; width: 332px; height: 61px;
    background: var(--paper); border-radius: 31px;
    display: flex; align-items: center; padding-left: 10px; gap: 12px;
  }
  .phone-pill svg { flex: none; }
  .phone-number { font-size: 40px; font-weight: 700; color: var(--ink); letter-spacing: -0.5px; }
  .service-grid { position: absolute; left: 482px; top: 30px; width: 536px; height: 300px; }
  .service {
    position: absolute; width: 140px; text-align: center;
    font-size: 15px; font-weight: 600; line-height: 1.2; color: var(--ink);
  }
  .service-icon {
    display: block; width: 68px; height: 68px; border-radius: 50%;
    margin: 0 auto 8px; background: radial-gradient(circle at 40% 35%, var(--pink), var(--pink-deep));
    box-shadow: 0 0 0 2px #f4c2cc;
  }
  .grid-rule { position: absolute; background: var(--rule); }

  /* Parking sign */
  .parking-sign { left: 47px; top: 948px; width: 1106px; height: 66px; }
  .parking-sign .brand-dot { left: 158px; top: 4px; width: 20px; height: 20px; }
  .parking-sign .brand-name { left: 40px; width: 250px; top: 27px; font-size: 26px; color: var(--paper); line-height: 1; }
  .parking-title {
    position: absolute; left: 371px; top: 7px; font-size: 44px; font-weight: 800;
    color: var(--pink); line-height: 1.2; letter-spacing: -0.5px;
  }
  .parking-icons { position: absolute; left: 795px; top: 8px; }
  .hours-pill {
    position: absolute; left: 900px; top: 10px; width: 168px; height: 46px;
    background: var(--sun); border-radius: 23px;
  }
  .hours-text {
    position: absolute; left: 934px; top: 3px; font-size: 42px; font-weight: 800;
    color: var(--ink); line-height: 1.4;
  }

  /* Roller door sign */
  .dropoff-sign { left: 110px; top: 1296px; width: 992px; height: 965px; }
  .dropoff-sign .brand-dot { left: 528px; top: 60px; width: 106px; height: 106px; }
  .dropoff-sign .brand-name { left: 0; width: 992px; top: 178px; font-size: 122px; color: var(--ink); line-height: 1; letter-spacing: -2px; }
  .dropoff-title {
    position: absolute; left: 0; width: 992px; text-align: center;
    font-weight: 800; line-height: 1; letter-spacing: -3px;
  }
  .dropoff-title.line-one { top: 585px; font-size: 148px; color: var(--paper); }
  .dropoff-title.line-two { top: 718px; font-size: 148px; color: var(--sun); }
</style>
</head>
<body>

  <p class="size-label" style="top:208px">2600MM (L) X 900MM (H)</p>
  <section class="sign door-sign">
    <svg class="backdrop" width="1049" height="363" viewBox="0 0 1049 363">
      <path d="M0 0 H378 C470 90 470 260 350 363 H0 Z" fill="var(--ink)"/>
      <path d="M378 0 C470 90 470 260 350 363" fill="none" stroke="var(--sky)" stroke-width="5"/>
      <path d="M392 0 C482 92 478 262 364 363" fill="none" stroke="var(--ink)" stroke-width="4" stroke-dasharray="40 10 18 8"/>
      <path d="M386 0 C477 92 474 262 358 363" fill="none" stroke="var(--paper)" stroke-width="3"/>
    </svg>
    <span class="brand-dot"></span>
    <p class="brand-name">Tallbrook</p>
    <div class="phone-pill">
      <svg width="34" height="34" viewBox="0 0 34 34" aria-hidden="true">
        <circle cx="17" cy="17" r="16" fill="var(--sky)"/>
        <path d="M11 9c1-1 2-1 3 0l2 3c.5 1 0 2-1 2.5 .8 2 2.3 3.5 4.3 4.3.5-1 1.5-1.5 2.5-1l3 2c1 1 1 2 0 3l-1.5 1.5C19 25 9 15 9.5 10.5Z" fill="var(--ink)"/>
      </svg>
      <span class="phone-number">1800 527 930</span>
    </div>

    <div class="service-grid">
      <span class="grid-rule" style="left:0;top:151px;width:536px;height:1px"></span>
      <span class="grid-rule" style="left:144px;top:0;width:1px;height:300px"></span>
      <span class="grid-rule" style="left:278px;top:0;width:1px;height:300px"></span>
      <span class="grid-rule" style="left:412px;top:0;width:1px;height:300px"></span>

      <div class="service" style="left:2px;top:8px"><span class="service-icon" role="img" aria-label="Social and living skills icon"></span>Social &amp; Living Skills Programs</div>
      <div class="service" style="left:141px;top:8px"><span class="service-icon" role="img" aria-label="Support workers icon"></span>Support Workers</div>
      <div class="service" style="left:275px;top:8px"><span class="service-icon" role="img" aria-label="Respite holidays icon"></span>Respite/ Supported Holidays</div>
      <div class="service" style="left:405px;top:8px"><span class="service-icon" role="img" aria-label="Exercise physiology icon"></span>Exercise Physiology</div>

      <div class="service" style="left:2px;top:165px"><span class="service-icon" role="img" aria-label="Occupational therapy icon"></span>Occupational Therapy</div>
      <div class="service" style="left:141px;top:165px"><span class="service-icon" role="img" aria-label="Speech therapy icon"></span>Speech Therapy</div>
      <div class="service" style="left:275px;top:165px"><span class="service-icon" role="img" aria-label="Psychology icon"></span>Psychology</div>
      <div class="service" style="left:405px;top:165px"><span class="service-icon" role="img" aria-label="Behavioural therapy icon"></span>Behavioural Therapy</div>
    </div>
  </section>

  <p class="size-label" style="top:865px">1000CM WIDE, 60CM HIGH</p>
  <section class="sign parking-sign">
    <svg class="backdrop" width="1106" height="66" viewBox="0 0 1106 66">
      <path d="M0 0 H306 C314 20 314 46 306 66 H0 Z" fill="var(--ink)"/>
      <path d="M306 0 C314 20 314 46 306 66" fill="none" stroke="var(--sky)" stroke-width="4"/>
      <path d="M312 0 C320 20 320 46 312 66" fill="none" stroke="var(--ink)" stroke-width="2"/>
    </svg>
    <span class="brand-dot"></span>
    <p class="brand-name">Tallbrook</p>
    <p class="parking-title">VISITOR PARKING</p>
    <svg class="parking-icons" width="110" height="52" viewBox="0 0 110 52" aria-hidden="true">
      <path d="M4 40 V28 L12 16 H38 L46 28 V40 Z" fill="none" stroke="var(--sky)" stroke-width="4" stroke-linejoin="round"/>
      <rect x="12" y="20" width="26" height="8" fill="var(--sky)"/>
      <circle cx="13" cy="40" r="5" fill="var(--sky)"/>
      <circle cx="37" cy="40" r="5" fill="var(--sky)"/>
      <rect x="50" y="6" width="14" height="16" rx="2" fill="var(--sky)"/>
      <text x="53" y="19" font-family="Poppins, sans-serif" font-weight="700" font-size="12" fill="#fff">P</text>
      <rect x="55" y="22" width="4" height="22" fill="var(--sky)"/>
      <circle cx="104" cy="28" r="20" fill="#fff" stroke="#2b3a8c" stroke-width="3"/>
      <rect x="100" y="3" width="8" height="4" fill="#2b3a8c"/>
      <path d="M104 16 V28" stroke="var(--pink)" stroke-width="2"/>
    </svg>
    <span class="hours-pill"></span>
    <p class="hours-text">24/7</p>
  </section>

  <p class="size-label" style="top:1224px">745CM WIDE BY 725CM HIGH</p>
  <section class="sign dropoff-sign">
    <svg class="backdrop" width="992" height="965" viewBox="0 0 992 965">
      <path d="M0 610 C140 440 320 380 496 380 C680 380 860 440 992 590 V965 H0 Z" fill="var(--ink)"/>
      <path d="M0 610 C140 440 320 380 496 380 C680 380 860 440 992 590" fill="none" stroke="var(--sun-line)" stroke-width="9"/>
      <path d="M10 585 C150 420 330 360 496 360 C680 360 860 420 992 560" fill="none" stroke="var(--ink)" stroke-width="4" stroke-dasharray="60 14 22 10"/>
    </svg>
    <span class="brand-dot"></span>
    <p class="brand-name">Tallbrook</p>
    <p class="dropoff-title line-one">DROP OFF</p>
    <p class="dropoff-title line-two">ZONE</p>
  </section>

</body>
</html>
```